Splashora water park letter head

the previous one need some update and to be fresh again.
attached is the previous design and want it something along the same way
logo on top and info in the bottom
attached also the logo in all formats.

Target Market(s)

official use

Font styles to use
Sans Serif

Requirements
Must have
• logo on top and as watermark
• website : www.splashora.ae
• address : P.O.Box 3867 Dubai - UAE
• email : info@splashora.ae
• social media links : splashorame
Nice to have
• something creative on the bottom
Should not have
• no phone numbers

```html
<!DOCTYPE html>
<html lang="en">
<head>
<meta charset="utf-8">
<title>Splashora Letterhead</title>
<link href="https://fonts.googleapis.com/css2?family=Open+Sans:wght@400;600;700&display=swap" rel="stylesheet">
<style>
  :root {
    --backdrop: #ececed;
    --paper: #ffffff;
    --ink: #3a3a3a;
    --ink-strong: #222222;
    --brand-blue: #1f7fcf;
    --brand-pink: #e0245e;
    --line-blue: #7cc3ee;
    --watermark: rgba(31, 127, 207, 0.08);
    --signature-fill: #f1f1f3;
  }
  * { box-sizing: border-box; margin: 0; padding: 0; }
  html, body {
    width: 1200px; height: 784px; overflow: hidden;
    background: var(--backdrop);
    font-family: "Open Sans", sans-serif;
  }
  .canvas {
    width: 1200px; height: 784px;
    display: flex; align-items: center; justify-content: center;
  }
  .letterhead {
    position: relative;
    width: 530px; height: 750px;
    background: var(--paper);
    box-shadow: 0 4px 18px rgba(0,0,0,0.12);
    overflow: hidden;
  }
  .brand {
    position: absolute; top: 40px; left: 44px;
    display: flex; align-items: center; gap: 7px;
  }
  .brand-dot {
    width: 14px; height: 14px; border-radius: 50%;
    background: var(--brand-pink);
  }
  .brand-name {
    font-size: 22px; font-weight: 700; color: var(--brand-pink);
    letter-spacing: 0.3px;
  }
  .watermark {
    position: absolute; top: 300px; left: 0; width: 100%;
    text-align: center;
    font-size: 92px; font-weight: 700;
    color: var(--watermark);
    pointer-events: none;
  }
  .letter {
    position: absolute; top: 120px; left: 74px; width: 390px;
    color: var(--ink);
    font-size: 9.2px; line-height: 1.5;
  }
  .salutation {
    font-size: 11.5px; font-weight: 700; color: var(--ink-strong);
    margin-bottom: 8px;
  }
  .letter p { margin: 0 0 11px 12px; }
  .signature {
    width: 120px; height: 58px; margin: 18px 0 0 20px;
    background: var(--signature-fill); border-radius: 4px;
  }
  .footer {
    position: absolute; left: 0; right: 0; bottom: 36px; height: 54px;
  }
  .footer-bar {
    position: absolute; left: 0; bottom: 0;
    width: 14px; height: 36px; background: var(--brand-pink);
  }
  .footer-info {
    position: absolute; left: 26px; bottom: 2px;
    font-size: 9px; line-height: 1.55; color: var(--ink);
  }
  .footer-info .label { font-weight: 700; color: var(--brand-blue); }
  .footer-line {
    position: absolute; left: 26px; right: 72px; bottom: 0;
    height: 1px; background: var(--line-blue);
  }
  .social-tab {
    position: absolute; right: 0; bottom: -9px;
    width: 78px; height: 18px;
    background: var(--brand-blue);
    clip-path: polygon(10px 0, 100% 0, 100% 100%, 10px 100%, 0 50%);
    display: flex; align-items: center; gap: 4px; padding-left: 14px;
    color: #fff; font-size: 6.5px; font-weight: 600;
  }
  .social-icon {
    width: 7px; height: 7px; border-radius: 50%; background: #fff;
  }
</style>
</head>
<body>
<main class="canvas">
  <article class="letterhead">
    <header class="brand">
      <span class="brand-dot"></span>
      <span class="brand-name">Splashora</span>
    </header>

    <div class="watermark" aria-hidden="true">Splashora</div>

    <section class="letter">
      <h2 class="salutation">Dear Mr. Adam,</h2>
      <p>Lorem Ipsum is simply dummy text of the printing and typesetting industry. Lorem Ipsum has been the industry's standard dummy text ever since the 1500s, when an unknown printer took a galley of type and scrambled it to make a type specimen book. It has survived not only five centuries, but also the leap into electronic typesetting, remaining essentially unchanged.</p>
      <p>The standard chunk of Lorem Ipsum used since the 1500s is reproduced below for those interested. Sections 1.10.32 and 1.10.33 from "de Finibus Bonorum et Malorum" by Cassian are also reproduced in their exact original form, accompanied by English versions from the 1914 translation by H. Marlow.</p>
      <p>Lorem Ipsum is simply dummy text of the printing and typesetting industry. Lorem Ipsum has been the industry's standard dummy text ever since the 1500s, when an unknown printer took a galley of type and scrambled it to make a type specimen book. It has survived not only five centuries, but also the leap into electronic typesetting, remaining essentially unchanged. It was popularised in the</p>
      <p>Lorem Ipsum is simply dummy text of the printing and typesetting industry. Lorem Ipsum has been the industry's standard dummy text ever since the 1500s, when an unknown printer took a galley of type and scrambled it to make a type specimen book. It has survived not only five centuries, but also the leap into electronic typesetting, remaining essentially unchanged. It was popularised in the</p>
      <p>Lorem Ipsum is simply dummy text of the printing and typesetting industry. Lorem Ipsum has been the industry's standard dummy text ever since the 1500s, when an unknown printer took a galley of type and scrambled it to make a type specimen book.</p>
      <div class="signature" role="img" aria-label="Handwritten signature of the sender"></div>
    </section>

    <footer class="footer">
      <div class="footer-bar"></div>
      <div class="footer-info">
        <div><span class="label">Splashora</span> P.O.Box 3867 Dubai - UAE</div>
        <div><span class="label">Mail:</span> info@splashora.ae &nbsp;<span class="label">Website:</span> www.splashora.ae</div>
      </div>
      <div class="footer-line"></div>
      <div class="social-tab">
        <span class="social-icon"></span>
        <span>splashorame</span>
      </div>
    </footer>
  </article>
</main>
</body>
</html>
```